New Modern Design Responsive Website For Mining Company

Hi there, we need a new custom designed website for an Australian Mining company that has just relaunched.

We have just completed a new logo design contest so that will be included for you to look at.

There is an existing site to look at https://www.veltorquarry.com/

Nothing should be assumed by this site other than that is the content we will be adding to it plus a blog as well. The current design and look is not at all what they want and hence why it should not be used as a base start for any new design.

They want a modern looking mobile friendly responsive design included website that appeals to the corporate market and stock investors.

They don't have a preference to colours used however colours that are considered more prestige / corporate / established and modern will most likely appeal. Colours like black/white, dark blue, gold , platinum etc would I think be more suitable but that is entirely up to you as they have not specified any colours at all.

The design should include mobile / tablet layout / design files.

If you have any questions, please get in touch any time. Thank you

Derek
Updates

Hi crew, Please confirm if you will included files for the mobile design as there has not been any mock ups from anyone showing the mobile version and how it would look? Thanks Derek

```html
<!DOCTYPE html>
<html lang="en">
<head>
<meta charset="utf-8">
<title>Veltor Quarry Ltd</title>
<link href="https://fonts.googleapis.com/css2?family=Red+Hat+Display:wght@400;500;600;700&display=swap" rel="stylesheet">
<style>
:root{
  --bg:#141414;
  --bg-deep:#0b0b0b;
  --yellow:#e6dc2e;
  --text:#d8d8d8;
  --muted:#a9a9a9;
  --white:#ffffff;
  --line:#5a5a5a;
}
*{margin:0;padding:0;box-sizing:border-box}
html,body{width:1200px;height:3609px;overflow:hidden}
body{background:var(--bg);font-family:"Red Hat Display",Arial,sans-serif;color:var(--text);position:relative}
.abs{position:absolute}
.hero-photo{left:0;top:0;width:1200px;height:860px;background:radial-gradient(ellipse at 75% 20%,#4a4a48 0%,#2a2a29 35%,#161616 75%,#141414 100%)}
.portfolio-photo{left:0;top:1480px;width:1200px;height:1500px;background:radial-gradient(ellipse at 60% 35%,#2c2c2a 0%,#1d1d1c 45%,#141414 80%)}
.contact-photo{left:0;top:2950px;width:1200px;height:600px;background:radial-gradient(ellipse at 45% 40%,#262625 0%,#181818 60%,#141414 100%)}
.info{font-size:13px;color:var(--muted);display:flex;align-items:center;gap:6px}
.info svg{width:11px;height:11px}
.info .call{color:var(--yellow);font-weight:700}
.topline{left:84px;top:46px;width:1036px;height:1px;background:#3a3a3a}
.brand{font-size:22px;font-weight:600;color:var(--white);letter-spacing:1px}
.nav{left:283px;top:75px;display:flex;gap:36px;font-size:15px;color:var(--white);letter-spacing:.3px}
.nav span{display:flex;align-items:center;gap:6px}
.btn-contact{left:1004px;top:65px;width:116px;height:40px;background:var(--yellow);color:#111;font-size:15px;display:flex;align-items:center;justify-content:center;font-weight:500}
.center{left:0;width:1200px;text-align:center}
.eyebrow{top:288px;font-size:20px;color:var(--white)}
.metals{top:320px;font-size:52px;font-weight:500;color:var(--white)}
.tagline{top:382px;font-size:50px;font-weight:600;color:var(--yellow)}
.lead{top:456px;font-size:16px;line-height:25px;color:var(--text)}
.btn{display:flex;align-items:center;justify-content:center;gap:12px;font-size:15px;border:1.5px solid var(--yellow);color:var(--text);letter-spacing:.3px}
.btn svg{width:18px;height:10px}
.btn.solid{background:var(--yellow);color:#111;font-weight:500}
.vline{left:600px;width:1px;background:#6a6a6a}
.section-title{font-size:50px;font-weight:500;color:var(--white)}
.section-title b{color:var(--yellow);font-weight:500}
.copy{font-size:16px;line-height:25px;color:var(--text)}
.objective{color:var(--yellow);font-weight:600;font-size:16px;line-height:25px}
.tile{top:1164px;width:314px;height:246px}
.project-img{left:214px;width:250px;height:250px;border-radius:50%}
.project-name{left:502px;font-size:41px;font-weight:600;color:var(--yellow)}
.project-copy{left:502px;font-size:15.5px;line-height:25px;color:var(--text);width:560px}
.project-btn{left:502px;width:174px;height:39px}
.form-title{left:84px;top:2966px;font-size:40px;font-weight:500;color:var(--white)}
.field{top:3046px;width:320px;height:35px;border-bottom:1px solid var(--line);font-size:14px;color:var(--muted)}
.divider{left:84px;top:3223px;width:1036px;height:1px;background:#8a8a8a}
.foot-col{top:3280px;font-size:15.5px;line-height:33px;color:var(--muted)}
.foot-col h4{color:var(--yellow);font-size:15.5px;font-weight:600;margin-bottom:4px}
.copyright{left:0;top:3551px;width:1200px;height:58px;background:var(--bg-deep);display:flex;align-items:center;justify-content:center;font-size:14px;color:var(--muted)}
</style>
</head>
<body>
<div class="abs hero-photo" role="img" aria-label="Dark photograph of a rocky mining landscape"></div>
<div class="abs portfolio-photo" role="img" aria-label="Faint dark photograph of heavy mining machinery"></div>
<div class="abs contact-photo" role="img" aria-label="Faint dark photograph of haul trucks at a mine site"></div>

<header>
  <div class="abs info" style="left:84px;top:16px"><svg viewBox="0 0 12 12"><path d="M6 11C3 7.5 2.5 6 2.5 4.5a3.5 3.5 0 0 1 7 0C9.5 6 9 7.5 6 11z" fill="none" stroke="#e6dc2e"/><circle cx="6" cy="4.5" r="1.2" fill="#e6dc2e"/></svg>SUITE 4.12B, LEVEL 4, HARBOUR COURT, 88 KESTREL STREET, SYDNEY NSW 2000</div>
  <div class="abs info" style="left:662px;top:16px"><svg viewBox="0 0 12 12"><circle cx="6" cy="6" r="5" fill="none" stroke="#e6dc2e"/><path d="M6 3v3l2 1.5" fill="none" stroke="#e6dc2e"/></svg>MON - FRI 8AM - 5PM</div>
  <div class="abs info" style="left:862px;top:16px"><span class="call">Call for a free estimate • 555 204 7781</span></div>
  <div class="abs topline"></div>
  <div class="abs brand" style="left:84px;top:70px">VELTOR QUARRY</div>
  <nav class="abs nav">
    <span>CORPORATE</span><span>GOVERNANCE</span><span>INVESTORS</span>
    <span>PORTFOLIO <svg width="10" height="6" viewBox="0 0 10 6"><path d="M0 0h10L5 6z" fill="#fff"/></svg></span>
    <span>ANNUAL REPORTS</span>
  </nav>
  <div class="abs btn-contact">CONTACT</div>
</header>

<section>
  <div class="abs center eyebrow">VELTOR ASX Code : VQR</div>
  <h1 class="abs center metals">CU Ni CO FE AU</h1>
  <h2 class="abs center tagline">Explorer -Emergent producer</h2>
  <p class="abs center lead">Lorem ipsum dolor sit amet, consectetur adipiscing elit, sed do eiusmod tempor incididunt<br>ut labore et dolore magna aliqua. Ut enim ad minim veniam, quis nostrud</p>
  <div class="abs btn" style="left:495px;top:593px;width:210px;height:39px">VIEW OUR WORKS <svg viewBox="0 0 18 10"><path d="M0 5h16M12 1l4 4-4 4" fill="none" stroke="#e6dc2e" stroke-width="1.5"/></svg></div>
  <div class="abs vline" style="top:659px;height:189px"></div>
</section>

<section>
  <h2 class="abs center section-title" style="top:878px">Our <b>Company</b></h2>
  <p class="abs center copy" style="top:965px">Veltor Quarry Ltd (company) is a public company listed on the Australian Securities<br>Exchange (ASX). The company ASX code is VQR. The company is focused on<br>mineral exploration and mining and in particular battery metals and gold.</p>
  <p class="abs center objective" style="top:1066px">Our objective is to commence mining and production and deliver shareholder<br>dividends as soon as is practicable.z</p>
  <div class="abs tile" style="left:84px;background:linear-gradient(135deg,#6b3320,#c8703f 50%,#8a3d22)" role="img" aria-label="Close-up of copper wire coils"></div>
  <div class="abs tile" style="left:443px;background:linear-gradient(135deg,#1c2a44,#5a86b8 50%,#1a2233)" role="img" aria-label="Close-up of blue metallic cobalt crystals"></div>
  <div class="abs tile" style="left:806px;background:linear-gradient(135deg,#2a2418,#c8a63a 50%,#3a301c)" role="img" aria-label="Gold nuggets in a pan"></div>
  <div class="abs vline" style="top:1462px;height:190px"></div>
</section>

<section>
  <h2 class="abs center section-title" style="top:1704px">Our <b>Portfolio</b></h2>
  <p class="abs center copy" style="top:1792px">Veltor Quarry Ltd (company) is a public company listed on the Australian Securities<br>Exchange (ASX). The company ASX code is VQR.</p>

  <div class="abs project-img" style="top:1890px;background:radial-gradient(circle,#9a7a5a,#7a5a3c 60%,#5a5a40)" role="img" aria-label="Aerial view of an open-cut mine road"></div>
  <h3 class="abs project-name" style="top:1932px">Kallindra</h3>
  <p class="abs project-copy" style="top:1994px">Lorem ipsum dolor sit amet, consectetur adipiscing elit, sed do<br>eiusmod tempor incididunt ut labore et dolore magna aliqua.</p>
  <div class="abs btn solid project-btn" style="top:2071px">VEW PROJECT <svg viewBox="0 0 18 10"><path d="M0 5h16M12 1l4 4-4 4" fill="none" stroke="#111" stroke-width="1.5"/></svg></div>

  <div class="abs project-img" style="top:2215px;background:linear-gradient(180deg,#c8ccd2 0%,#8a8a7a 40%,#6a6a50 70%,#5a5048)" role="img" aria-label="Hillside with old stone ruins"></div>
  <h3 class="abs project-name" style="top:2257px">Mt. Harlan</h3>
  <p class="abs project-copy" style="top:2319px">Lorem ipsum dolor sit amet, consectetur adipiscing elit, sed do<br>eiusmod tempor incididunt ut labore et dolore magna aliqua.</p>
  <div class="abs btn project-btn" style="top:2396px">VEW PROJECT <svg viewBox="0 0 18 10"><path d="M0 5h16M12 1l4 4-4 4" fill="none" stroke="#e6dc2e" stroke-width="1.5"/></svg></div>

  <div class="abs project-img" style="top:2540px;background:linear-gradient(180deg,#b8c4d0 0%,#a08a70 35%,#8a7a3a 65%,#5a4a22)" role="img" aria-label="Granite mountain above farmland"></div>
  <h3 class="abs project-name" style="top:2582px">Orvane</h3>
  <p class="abs project-copy" style="top:2644px">Lorem ipsum dolor sit amet, consectetur adipiscing elit, sed do<br>eiusmod tempor incididunt ut labore et dolore magna aliqua.</p>
  <div class="abs btn project-btn" style="top:2721px;border-color:#a8a030;color:#9a9a9a">VIEW PROJECT <svg viewBox="0 0 18 10"><path d="M0 5h16M12 1l4 4-4 4" fill="none" stroke="#9a9a9a" stroke-width="1.5"/></svg></div>
</section>

<section>
  <h2 class="abs form-title">Ready to work with us?</h2>
  <div class="abs field" style="left:84px">Full Name</div>
  <div class="abs field" style="left:440px">Email Address</div>
  <div class="abs field" style="left:801px">Contact Number</div>
  <div class="abs btn" style="left:84px;top:3128px;width:210px;height:39px">REQUEST A QUOTE <svg viewBox="0 0 18 10"><path d="M0 5h16M12 1l4 4-4 4" fill="none" stroke="#e6dc2e" stroke-width="1.5"/></svg></div>
</section>

<footer>
  <div class="abs divider"></div>
  <div class="abs brand" style="left:84px;top:3280px;font-size:19px">VELTOR QUARRY</div>
  <div class="abs foot-col" style="left:294px"><h4>CORPORATE</h4>Our Team<br>About Us</div>
  <div class="abs foot-col" style="left:456px"><h4>GOVERNANCE</h4>Notices<br>Text<br>Text</div>
  <div class="abs foot-col" style="left:631px"><h4>INVESTORS</h4>Investors<br>Meeting Notices<br>Others</div>
  <div class="abs foot-col" style="left:819px"><h4>PORTFOLIO</h4>Kallindra<br>Mt. Harlan<br>Orvane</div>
  <div class="abs foot-col" style="left:976px"><h4>ANNUAL REPORTS</h4>Latest Reports<br>Report Archive<br>Text</div>
  <div class="abs info" style="left:82px;top:3511px"><svg viewBox="0 0 12 12"><path d="M6 11C3 7.5 2.5 6 2.5 4.5a3.5 3.5 0 0 1 7 0C9.5 6 9 7.5 6 11z" fill="none" stroke="#e6dc2e"/><circle cx="6" cy="4.5" r="1.2" fill="#e6dc2e"/></svg>SUITE 4.12B, LEVEL 4, HARBOUR COURT, 88 KESTREL STREET, SYDNEY NSW 2000</div>
  <div class="abs info" style="left:659px;top:3511px"><svg viewBox="0 0 12 12"><circle cx="6" cy="6" r="5" fill="none" stroke="#e6dc2e"/><path d="M6 3v3l2 1.5" fill="none" stroke="#e6dc2e"/></svg>MON - FRI 8AM - 5PM</div>
  <div class="abs info" style="left:860px;top:3511px"><span class="call">Call for a free estimate • 555 204 7781</span></div>
  <div class="abs copyright">Copyright © 2022 Veltorquarry LTD</div>
</footer>
</body>
</html>
```